Website for Corvalind Capital, my new firm that raises money from investors to buy, build, own an...

Corvalind Capital needs a website! We are a new company with very experienced people, who invest in, own and build hotel properties, as well as apartments and other commercial real estate. We seek investors for our projects, and we provide safe, secure returns on their investment in our projects. Our new logo is designed to exhibit strength, class and security, and would like our website to continue on this theme. Our name, Corvalind, is a word-play on a Greek word “aristeia”, which means “excellence” and “a warriors finest moment of glory in war”. If you are in business, you realize that much of it is like war, with strategy and moves and opponents and competitors, and ever-changing economic conditions and threats that make business very much like war. We like to think that we are good at business (war), and so have named our company “Corvalind”, using the founders last name and the word “aristeia” combined. Another definition of "aristeia" is "performing at the peak of one's potential after a long struggle"...again, much like business in real life! The website design should exhibit financial security, smart moves, and positive growth towards a bright future.

Target Market(s)

The target market is smart and wealthy investors, with others such as brokers, cities and government agencies, lenders, sellers, partners, etc also looking at it.

Industry/Entity Type

Investment

Number of Pages Required

5+ page

Font styles to use
Sans Serif

Colors
fec214

Requirements
Must have
• Our website should have a landing page, a "about" or bio page, a projects page and a contact us page. Our new logo uses the colors black and gold, so this should be factored in to our site. The site should be simple, yet impactful and impressive. I have actually two logos, which can be mixed and interchanged in a complimentary way, each with their own unique look.
Nice to have
• I have uploaded a couple screenshots of a website i like, and the simplicity I mention.
Should not have
• The site should not be flashy or complicated or complex or "busy"

```html
<!DOCTYPE html>
<html lang="en">
<head>
<meta charset="utf-8">
<title>Corvalind Capital — Contact Us</title>
<link rel="stylesheet" href="https://fonts.googleapis.com/css2?family=Marcellus&family=Libre+Baskerville:wght@400;700&family=Montserrat:ital,wght@0,600;1,600&display=swap">
<style>
  :root {
    --gold: #fec214;
    --gold-deep: #c9a23a;
    --ink: #1c1c1c;
    --panel: #262626;
    --paper: #ffffff;
  }
  * { margin: 0; padding: 0; box-sizing: border-box; }
  html, body { width: 1200px; height: 1200px; overflow: hidden; background: var(--paper); }
  body { position: relative; font-family: "Libre Baskerville", Georgia, serif; color: var(--ink); }

  .brand { position: absolute; left: 150px; top: 8px; display: flex; align-items: center; gap: 6px;
    font-family: "Marcellus", serif; font-size: 15px; letter-spacing: 1.5px; color: var(--ink); }
  .brand-mark { width: 10px; height: 10px; background: var(--gold); }

  .main-nav { position: absolute; left: 150px; top: 40px; width: 855px; height: 21px;
    border-bottom: 3px solid var(--gold); display: flex; padding-left: 90px; }
  .main-nav a { flex: 1; text-align: center; font-family: "Marcellus", serif; font-size: 10.5px; color: var(--ink);
    text-decoration: none; border-right: 4px solid var(--gold); line-height: 22px; letter-spacing: .5px; }

  .hero { position: absolute; left: 0; top: 74px; width: 1200px; height: 162px;
    background: linear-gradient(100deg, #b98e72 0%, #3b4650 18%, #1f2b36 55%, #2c3d4c 100%); }
  .hero-copy { position: absolute; left: 609px; top: 6px; width: 436px; color: #fff;
    font-size: 14.5px; line-height: 14px; font-family: "Libre Baskerville", serif; }
  .btn { display: inline-block; background: var(--gold); color: #fff; text-align: center;
    font-family: "Marcellus", serif; font-size: 8px; text-decoration: none; }
  .hero-join { position: absolute; left: 540px; top: 145px; width: 82px; height: 12px; line-height: 12px; }

  .section-title { position: absolute; left: 0; width: 1200px; text-align: center;
    font-family: "Marcellus", serif; font-weight: 400; font-size: 19px; color: var(--gold-deep); letter-spacing: 1px; }
  .section-title span { border-bottom: 2px solid var(--gold-deep); }

  .dept { position: absolute; width: 410px; }
  .dept h2 { margin-left: 19px; width: 262px; height: 16px; background: var(--gold); color: #fff;
    font-family: "Marcellus", serif; font-weight: 400; font-size: 12px; text-align: center; line-height: 16px; letter-spacing: 1px; }
  .dept p { margin-top: 7px; font-size: 6.8px; font-weight: 700; letter-spacing: .55px; line-height: 12px; height: 84px; overflow: hidden; }
  .dept .mail { margin-top: 1px; font-size: 6.8px; font-weight: 700; letter-spacing: .55px; line-height: 9px; }

  .contact-form { position: absolute; left: 150px; top: 548px; width: 900px; height: 104px; background: var(--panel); }
  .field { position: absolute; left: 37px; width: 454px; height: 12px; background: var(--gold); color: #fff;
    font-family: "Marcellus", serif; font-size: 8.5px; padding-left: 5px; line-height: 12px; }
  .message { position: absolute; left: 518px; top: 9px; width: 344px; height: 85px; background: var(--gold);
    color: #fff; font-family: "Marcellus", serif; font-size: 8.5px; padding: 3px 12px; }
  .send { position: absolute; left: 248px; top: 81px; width: 82px; height: 13px; line-height: 13px; }

  .faq { position: absolute; width: 380px; font-size: 7.4px; letter-spacing: .45px; }
  .faq h3 { font-weight: 400; font-size: 7.8px; line-height: 10px; height: 10px; }
  .faq p { line-height: 7.6px; height: 48px; overflow: hidden; margin-bottom: 4px; }
  .faq p.short { height: 24px; }

  .site-footer { position: absolute; left: 0; top: 1133px; width: 1200px; height: 67px; background: var(--panel);
    color: #fff; font-family: "Montserrat", sans-serif; }
  .site-footer h4 { font-style: italic; font-weight: 600; font-size: 10px; letter-spacing: 1px; line-height: 12px; }
  .foot-contact { position: absolute; left: 175px; top: 2px; font-size: 8px; }
  .foot-contact h4 { margin-left: 41px; }
  .foot-contact ul { list-style: none; }
  .foot-contact li { display: flex; align-items: center; gap: 12px; height: 12px; letter-spacing: .8px; }
  .foot-menu { position: absolute; left: 411px; top: 2px; font-size: 7.5px; font-style: italic; line-height: 8.8px; }
  .foot-menu ul { list-style: none; }
  .foot-social { position: absolute; left: 545px; top: 2px; width: 140px; height: 50px; font-size: 6px; font-style: italic; }
  .foot-social ul { list-style: none; position: absolute; left: 0; top: 13px; }
  .foot-social li { display: flex; align-items: center; gap: 34px; height: 13px; line-height: 8px; }
  .social-dot { width: 13px; height: 11px; border: 1.5px solid #fff; border-radius: 50%; flex: none; }
  .subscribe-email { position: absolute; left: 712px; top: 19px; width: 240px; height: 18px; background: #fff;
    color: #555; font-size: 6px; padding-left: 10px; line-height: 26px; font-style: italic; }
  .subscribe-btn { position: absolute; left: 961px; top: 19px; width: 78px; height: 18px; line-height: 18px;
    background: var(--gold-deep); font-family: "Montserrat", sans-serif; font-size: 6px; }
  .legal { position: absolute; top: 60px; font-size: 4.5px; line-height: 5px; }
</style>
</head>
<body>

<header>
  <div class="brand"><span class="brand-mark"></span>CORVALIND</div>
  <nav class="main-nav">
    <a href="#">Home</a><a href="#">Portfolio</a><a href="#">What We Do</a><a href="#">About Us</a><a href="#">Careers</a><a href="#">Contact</a>
  </nav>
</header>

<section class="hero" role="img" aria-label="Photograph of a hand placing large white letters spelling HELLO on a dark slate surface">
  <p class="hero-copy">Lorem ipsum dolor sit amet, consectetur adipisicing elit, sed do eiusmod tempor incididunt ut labore et dolore magna aliqua. Ut enim ad minim veniam, quis nostrud exercitation ullamco laboris nisi ut aliquip ex ea commodo consequat. Duis aute irure dolor in</p>
  <a class="btn hero-join">Join Now</a>
</section>

<h1 class="section-title" style="top:254px"><span>Contact Us</span></h1>

<article class="dept" style="left:154px;top:282px"><h2>How to Buy for Business</h2><p>Lorem ipsum dolor sit amet, consectetur adipisicing elit, sed do eiusmod tempor incididunt ut labore et dolore magna aliqua. Ut enim ad minim veniam, quis nostrud exercitation ullamco laboris nisi ut aliquip ex ea commodo consequat. Duis aute irure dolor in reprehenderit in voluptate velit esse cillum dolore eu fugiat nulla pariatur. Excepteur sint occaecat cupidatat non proident, sunt in culpa qui officia deserunt mollit anim id est laborum. Sed ut perspiciatis unde omnis iste natus error sit voluptatem accusantium doloremque laudantium, totam rem aperiam, eaque ipsa quae</p><div class="mail">Email:hello@corvalindcapital.com</div></article>
<article class="dept" style="left:639px;top:282px"><h2>Customer Service</h2><p>Lorem ipsum dolor sit amet, consectetur adipisicing elit, sed do eiusmod tempor incididunt ut labore et dolore magna aliqua. Ut enim ad minim veniam, quis nostrud exercitation ullamco laboris nisi ut aliquip ex ea commodo consequat. Duis aute irure dolor in reprehenderit in voluptate velit esse cillum dolore eu fugiat nulla pariatur. Excepteur sint occaecat cupidatat non proident, sunt in culpa qui officia deserunt mollit anim id est laborum. Sed ut perspiciatis unde omnis iste natus error sit voluptatem accusantium doloremque laudantium, totam rem aperiam, eaque ipsa quae</p><div class="mail">Email:hello@corvalindcapital.com</div></article>
<article class="dept" style="left:154px;top:421px"><h2>Sponsorship</h2><p>Lorem ipsum dolor sit amet, consectetur adipisicing elit, sed do eiusmod tempor incididunt ut labore et dolore magna aliqua. Ut enim ad minim veniam, quis nostrud exercitation ullamco laboris nisi ut aliquip ex ea commodo consequat. Duis aute irure dolor in reprehenderit in voluptate velit esse cillum dolore eu fugiat nulla pariatur. Excepteur sint occaecat cupidatat non proident, sunt in culpa qui officia deserunt mollit anim id est laborum. Sed ut perspiciatis unde omnis iste natus error sit voluptatem accusantium doloremque laudantium, totam rem aperiam, eaque ipsa quae</p><div class="mail">Email:hello@corvalindcapital.com</div></article>
<article class="dept" style="left:639px;top:421px"><h2>Media Relations</h2><p>Lorem ipsum dolor sit amet, consectetur adipisicing elit, sed do eiusmod tempor incididunt ut labore et dolore magna aliqua. Ut enim ad minim veniam, quis nostrud exercitation ullamco laboris nisi ut aliquip ex ea commodo consequat. Duis aute irure dolor in reprehenderit in voluptate velit esse cillum dolore eu fugiat nulla pariatur. Excepteur sint occaecat cupidatat non proident, sunt in culpa qui officia deserunt mollit anim id est laborum. Sed ut perspiciatis unde omnis iste natus error sit voluptatem accusantium doloremque laudantium, totam rem aperiam, eaque ipsa quae</p><div class="mail">Email:hello@corvalindcapital.com</div></article>

<form class="contact-form">
  <div class="field" style="top:11px">Name</div>
  <div class="field" style="top:30px;left:36px">Email</div>
  <div class="field" style="top:48px;left:36px">Phone</div>
  <div class="message">Message...</div>
  <a class="btn send">Send</a>
</form>

<article class="dept" style="left:154px;top:672px"><h2>Investor Relations</h2><p>Lorem ipsum dolor sit amet, consectetur adipisicing elit, sed do eiusmod tempor incididunt ut labore et dolore magna aliqua. Ut enim ad minim veniam, quis nostrud exercitation ullamco laboris nisi ut aliquip ex ea commodo consequat. Duis aute irure dolor in reprehenderit in voluptate velit esse cillum dolore eu fugiat nulla pariatur. Excepteur sint occaecat cupidatat non proident, sunt in culpa qui officia deserunt mollit anim id est laborum. Sed ut perspiciatis unde omnis iste natus error sit voluptatem accusantium doloremque laudantium, totam rem aperiam, eaque ipsa quae</p><div class="mail">Email:hello@corvalindcapital.com</div></article>
<article class="dept" style="left:639px;top:672px"><h2>Consumer Affairs</h2><p>Lorem ipsum dolor sit amet, consectetur adipisicing elit, sed do eiusmod tempor incididunt ut labore et dolore magna aliqua. Ut enim ad minim veniam, quis nostrud exercitation ullamco laboris nisi ut aliquip ex ea commodo consequat. Duis aute irure dolor in reprehenderit in voluptate velit esse cillum dolore eu fugiat nulla pariatur. Excepteur sint occaecat cupidatat non proident, sunt in culpa qui officia deserunt mollit anim id est laborum. Sed ut perspiciatis unde omnis iste natus error sit voluptatem accusantium doloremque laudantium, totam rem aperiam, eaque ipsa quae</p><div class="mail">Email:hello@corvalindcapital.com</div></article>
<article class="dept" style="left:154px;top:810px"><h2>Sustainability</h2><p>Lorem ipsum dolor sit amet, consectetur adipisicing elit, sed do eiusmod tempor incididunt ut labore et dolore magna aliqua. Ut enim ad minim veniam, quis nostrud exercitation ullamco laboris nisi ut aliquip ex ea commodo consequat. Duis aute irure dolor in reprehenderit in voluptate velit esse cillum dolore eu fugiat nulla pariatur. Excepteur sint occaecat cupidatat non proident, sunt in culpa qui officia deserunt mollit anim id est laborum. Sed ut perspiciatis unde omnis iste natus error sit voluptatem accusantium doloremque laudantium, totam rem aperiam, eaque ipsa quae</p><div class="mail">Email:hello@corvalindcapital.com</div></article>
<article class="dept" style="left:639px;top:810px"><h2>Environments</h2><p>Lorem ipsum dolor sit amet, consectetur adipisicing elit, sed do eiusmod tempor incididunt ut labore et dolore magna aliqua. Ut enim ad minim veniam, quis nostrud exercitation ullamco laboris nisi ut aliquip ex ea commodo consequat. Duis aute irure dolor in reprehenderit in voluptate velit esse cillum dolore eu fugiat nulla pariatur. Excepteur sint occaecat cupidatat non proident, sunt in culpa qui officia deserunt mollit anim id est laborum. Sed ut perspiciatis unde omnis iste natus error sit voluptatem accusantium doloremque laudantium, totam rem aperiam, eaque ipsa quae</p><div class="mail">Email:hello@corvalindcapital.com</div></article>

<h1 class="section-title" style="top:928px"><span>FAQ</span></h1>

<div class="faq" style="left:153px;top:962px">
  <h3>Where We Invest</h3><p>Lorem ipsum dolor sit amet, consectetur adipisicing elit, sed do eiusmod tempor incididunt ut labore et dolore magna aliqua. Ut enim ad minim veniam, quis nostrud exercitation ullamco laboris nisi ut aliquip ex ea commodo consequat. Duis aute irure dolor in reprehenderit in voluptate velit esse cillum dolore eu fugiat nulla pariatur. Excepteur sint occaecat cupidatat non proident, sunt in culpa qui officia deserunt mollit anim id est</p>
  <h3>What We Invest</h3><p>Lorem ipsum dolor sit amet, consectetur adipisicing elit, sed do eiusmod tempor incididunt ut labore et dolore magna aliqua. Ut enim ad minim veniam, quis nostrud exercitation ullamco laboris nisi ut aliquip ex ea commodo consequat. Duis aute irure dolor in reprehenderit in voluptate velit esse cillum dolore eu fugiat nulla pariatur. Excepteur sint occaecat cupidatat non proident, sunt in culpa qui officia deserunt mollit anim id est</p>
  <h3>Our Partners</h3><p class="short">Lorem ipsum dolor sit amet, consectetur adipisicing elit, sed do eiusmod tempor incididunt ut labore et dolore magna aliqua. Ut enim ad minim veniam, quis nostrud exercitation ullamco laboris nisi ut aliquip ex ea</p>
</div>
<div class="faq" style="left:670px;top:962px">
  <h3>Return</h3><p>Lorem ipsum dolor sit amet, consectetur adipisicing elit, sed do eiusmod tempor incididunt ut labore et dolore magna aliqua. Ut enim ad minim veniam, quis nostrud exercitation ullamco laboris nisi ut aliquip ex ea commodo consequat. Duis aute irure dolor in reprehenderit in voluptate velit esse cillum dolore eu fugiat nulla pariatur. Excepteur sint occaecat cupidatat non proident, sunt in culpa qui officia deserunt mollit anim id est</p>
  <h3>How Do I Invest</h3><p>Lorem ipsum dolor sit amet, consectetur adipisicing elit, sed do eiusmod tempor incididunt ut labore et dolore magna aliqua. Ut enim ad minim veniam, quis nostrud exercitation ullamco laboris nisi ut aliquip ex ea commodo consequat. Duis aute irure dolor in reprehenderit in voluptate velit esse cillum dolore eu fugiat nulla pariatur. Excepteur sint occaecat cupidatat non proident, sunt in culpa qui officia deserunt mollit anim id est</p>
  <h3>History</h3><p class="short">Lorem ipsum dolor sit amet, consectetur adipisicing elit, sed do eiusmod tempor incididunt ut labore et dolore magna aliqua. Ut enim ad minim veniam, quis nostrud exercitation ullamco laboris nisi ut aliquip ex ea</p>
</div>

<footer class="site-footer">
  <div class="foot-contact">
    <h4>Contact Us</h4>
    <ul>
      <li><svg width="20" height="11" viewBox="0 0 20 11"><path d="M1 4 L10 0 L19 4 Z M3 5 V10 M7 5 V10 M13 5 V10 M17 5 V10 M1 10.5 H19" stroke="#fff" fill="none"/></svg><i>Adress:48 Harlow Ave</i></li>
      <li><svg width="20" height="11" viewBox="0 0 20 11"><rect x="2" y="1" width="16" height="9" stroke="#fff" fill="none"/><path d="M2 1 L10 7 L18 1" stroke="#fff" fill="none"/></svg>Email:info@</li>
      <li><svg width="20" height="11" viewBox="0 0 20 11"><path d="M4 1 C2 3 4 8 9 10 L11 8 L9 6 L7 7 C6 6 5 5 5 4 L6 2 Z" fill="#fff"/></svg>Phone:555-014-2270</li>
    </ul>
  </div>
  <div class="foot-menu">
    <h4>Menu</h4>
    <ul><li>About</li><li>Community</li><li>Resources</li><li>Services</li><li>Citie</li></ul>
  </div>
  <div class="foot-social">
    <h4>Connect With Us</h4>
    <ul>
      <li><span class="social-dot"></span>Gallery</li>
      <li><span class="social-dot"></span>Updates</li>
      <li><span class="social-dot"></span>Community</li>
    </ul>
  </div>
  <div class="subscribe-email">Email</div>
  <a class="btn subscribe-btn">Subscribe</a>
  <span class="legal" style="left:502px">Site Terms</span>
  <span class="legal" style="left:574px">Site Disclosures</span>
  <span class="legal" style="left:673px">Help</span>
</footer>

</body>
</html>
```